KELTO Robotics Engineering Design Team - Pull Up Banner Design

I need a pull-up banner design which I can use at trade shows and events to market our research and development group. We are specialist design engineers who have expertise in:
- Embedded Electronics and Circuit Design
- Rapid Functional Prototyping
- Sensor and Vision Systems
- Robotics Systems

Recent projects include:
- Robotic concrete sewer probes
- IoT wildlife tracking systems
- Robots for exploring wombat burrows
- Smart pest control technology

Target Market(s)

Potential clients who want us to design a project for them

Industry/Entity Type

Engineering Consulting

Colors

Designer to choose colors to be used in the design.

Requirements
Must have
• Look professional and have a high-tech feel to it

```html
<!DOCTYPE html>
<html lang="en">
<head>
<meta charset="utf-8">
<title>KELTO Pull Up Banner</title>
<link rel="stylesheet" href="https://fonts.googleapis.com/css2?family=Open+Sans:wght@400;600;700&display=swap">
<style>
  :root {
    --page-bg: #dedddb;
    --brand-blue: #3a4fa3;
    --brand-red: #c4303c;
    --ink: #1c1c1c;
    --white: #ffffff;
    --photo-sky: #a9c3e3;
    --photo-mid: #8d8a6e;
    --photo-ground: #6d7a48;
  }
  * { margin: 0; padding: 0; box-sizing: border-box; }
  html, body {
    width: 1200px; height: 1200px; overflow: hidden;
    background: var(--page-bg);
    font-family: "Open Sans", Arial, sans-serif;
  }
  .banner-frame {
    position: absolute; left: 397px; top: 93px;
    width: 406px; height: 1015px; overflow: hidden;
  }
  .banner {
    position: absolute; left: 0; top: 0;
    width: 654px; height: 1635px;
    background: var(--white);
    transform: scale(0.6208); transform-origin: 0 0;
  }
  .banner-shapes { position: absolute; inset: 0; }
  .brand {
    position: absolute; left: 330px; top: 640px; width: 320px;
    text-align: center; color: var(--white);
  }
  .brand-name {
    font-weight: 700; font-size: 50px; letter-spacing: 10px; line-height: 1;
    margin-bottom: 14px;
  }
  .brand-services { font-size: 12.5px; font-weight: 400; line-height: 16px; letter-spacing: 0.3px; }
  .brand-web { font-size: 15.5px; font-weight: 600; margin-top: 2px; }
  .section-title {
    position: absolute; left: 48px;
    color: var(--brand-red); font-weight: 700; font-size: 40px; line-height: 52px;
  }
  .title-expertise { top: 852px; }
  .title-projects { top: 1205px; }
  .check-list { position: absolute; left: 48px; list-style: none; }
  .list-expertise { top: 1030px; }
  .list-projects { top: 1279px; }
  .check-list li {
    display: flex; align-items: center; gap: 20px;
    font-size: 27px; color: var(--ink); height: 39px;
  }
  .check-list svg { width: 20px; height: 20px; flex: none; }
  .site-url {
    position: absolute; left: 0; width: 654px; top: 1548px;
    text-align: center; color: var(--white);
    font-size: 28px; letter-spacing: 2.5px; font-weight: 400;
  }
  .site-url strong { font-weight: 700; }
</style>
</head>
<body>
  <div class="banner-frame">
    <div class="banner">
      <svg class="banner-shapes" viewBox="0 0 654 1635" width="654" height="1635">
        <defs>
          <linearGradient id="photoTone" x1="0" y1="0" x2="0" y2="1">
            <stop offset="0" stop-color="var(--photo-sky)"/>
            <stop offset="0.3" stop-color="#c9c6be"/>
            <stop offset="0.55" stop-color="var(--photo-mid)"/>
            <stop offset="1" stop-color="var(--photo-ground)"/>
          </linearGradient>
          <symbol id="tick-bullet" viewBox="0 0 20 20">
            <circle cx="10" cy="10" r="9" fill="var(--brand-blue)"/>
            <path d="M5.5 10 L9 13.5 L15 6" fill="none" stroke="var(--brand-red)" stroke-width="2.6" stroke-linecap="round" stroke-linejoin="round"/>
          </symbol>
        </defs>
        <polygon class="photo-area" role="img"
          aria-label="Photo: engineering team in hi-vis vests around a tripod-mounted robotic probe over a concrete sewer access point, utility truck and stacked crates behind"
          points="0,0 654,0 654,520 215,712 0,795" fill="url(#photoTone)"/>
        <polygon class="accent-blue-wedge" points="654,520 190,695 654,930" fill="var(--brand-blue)"/>
        <polygon class="accent-red-stripe" points="190,692 654,928 654,942 182,698" fill="var(--brand-red)"/>
        <polygon class="accent-blue-line" points="0,582 196,692 190,700 0,594" fill="var(--brand-blue)"/>
        <polygon class="accent-red-wedge" points="0,613 190,705 0,782" fill="var(--brand-red)"/>
        <polygon class="footer-blue" points="0,1467 654,1535 654,1635 0,1635" fill="var(--brand-blue)"/>
        <polygon class="footer-red" points="654,1405 654,1635 251,1635" fill="var(--brand-red)"/>
      </svg>

      <div class="brand">
        <div class="brand-name">KELTO</div>
        <div class="brand-services">ROBOTICS | AUTOMATION | MECHATRONICS</div>
        <div class="brand-services">PROTOTYPING | SENSING</div>
        <div class="brand-web">keltolaboratory.com</div>
      </div>

      <h2 class="section-title title-expertise">We are specialist<br>design engineers who<br>have expertise in:</h2>
      <ul class="check-list list-expertise">
        <li><svg><use href="#tick-bullet"/></svg>Embedded Electronics and Circuit Design</li>
        <li><svg><use href="#tick-bullet"/></svg>Rapid Functional Prototyping</li>
        <li><svg><use href="#tick-bullet"/></svg>Sensor and Vision Systems</li>
        <li><svg><use href="#tick-bullet"/></svg>Robotics Systems</li>
      </ul>

      <h2 class="section-title title-projects">Recent projects include:</h2>
      <ul class="check-list list-projects">
        <li><svg><use href="#tick-bullet"/></svg>Robotic concrete sewer probes</li>
        <li><svg><use href="#tick-bullet"/></svg>IoT wildlife tracking systems</li>
        <li><svg><use href="#tick-bullet"/></svg>Robots for exploring wombat burrows</li>
        <li><svg><use href="#tick-bullet"/></svg>Smart pest control technology</li>
      </ul>

      <div class="site-url">www.<strong>keltolaboratory</strong>.com</div>
    </div>
  </div>
</body>
</html>
```